MK Tallow Insurance - Aviation

We are wanting to have new business cards designed for our new aviation division. We currently have business cards for the other business (attached). We would like to use the same colors and have the logo somewhere on the business card along with a small, single engine airplane, maybe in the background but would like it to be different than the original and more focused on aviation. Also wondering if there is a way to do laser cut and make the business card in the shape of an airplane? Just some different ideas that make it stand out.

Target Market(s)

Pilots

Industry/Entity Type

Insurance

Contact Information for Business Card

We would like to use the same colors and have the logo somewhere on the business card along with a small, single engine airplane, maybe in the background but would like it to be different than the original and more focused on aviation. Also wondering if there is a way to do laser cut and make the business card in the shape of an airplane? Just some different ideas that make it stand out.

Requirements
Must have
• A small, single engine airplane

```html
<!DOCTYPE html>
<html lang="en">
<head>
<meta charset="utf-8">
<title>MK Tallow Insurance – Business Card</title>
<link rel="stylesheet" href="https://fonts.googleapis.com/css2?family=Cinzel:wght@400;600&family=Poppins:wght@400;500&display=swap">
<style>
  :root {
    --page-bg: #c9c9cb;
    --card-black: #151516;
    --accent-pink: #e0104f;
    --text-white: #f2f2f2;
    --text-grey: #d8d8d8;
    --sky-deep: #1f6fd0;
    --sky-mid: #3d94e6;
    --sky-light: #8cc4f2;
    --plane-white: #f4f6f8;
    --plane-grey: #b9c2cc;
    --logo-navy: #0d1730;
  }
  * { margin: 0; padding: 0; box-sizing: border-box; }
  html, body { width: 1200px; height: 800px; overflow: hidden; }
  body {
    background: var(--page-bg);
    display: flex;
    align-items: center;
    justify-content: center;
    gap: 56px;
    font-family: "Poppins", sans-serif;
  }
  .card {
    position: relative;
    width: 525px;
    height: 300px;
    border-bottom: 3px solid var(--accent-pink);
    border-left: 3px solid var(--accent-pink);
    box-shadow: 0 10px 24px rgba(0,0,0,0.25);
    overflow: hidden;
  }

  /* Front */
  .card-front { background: var(--card-black); color: var(--text-white); }
  .brand {
    position: absolute;
    top: 62px;
    right: 40px;
    display: flex;
    align-items: center;
    gap: 12px;
  }
  .brand-dot {
    width: 16px;
    height: 16px;
    border-radius: 50%;
    background: var(--accent-pink);
    flex: none;
  }
  .brand-name {
    font-family: "Cinzel", serif;
    font-weight: 400;
    font-size: 24px;
    letter-spacing: 1.5px;
    color: var(--text-white);
    white-space: nowrap;
  }
  .divider-main {
    position: absolute;
    left: 30px;
    right: 22px;
    top: 148px;
    height: 1px;
    background: var(--accent-pink);
  }
  .person {
    position: absolute;
    left: 30px;
    top: 162px;
  }
  .person-name {
    font-family: "Cinzel", serif;
    font-weight: 400;
    font-size: 24px;
    color: var(--accent-pink);
    letter-spacing: 0.5px;
    line-height: 1;
  }
  .person-title {
    font-size: 12.5px;
    color: var(--text-grey);
    margin-top: 3px;
  }
  .divider-person {
    width: 235px;
    height: 1px;
    background: var(--accent-pink);
    margin: 8px 0 7px;
  }
  .contact-list { list-style: none; }
  .contact-list li {
    display: flex;
    align-items: center;
    gap: 10px;
    font-size: 12.5px;
    line-height: 19px;
    color: var(--text-white);
  }
  .contact-list svg { width: 11px; height: 11px; flex: none; }
  .address {
    position: absolute;
    right: 26px;
    top: 164px;
    text-align: right;
    font-style: normal;
    font-size: 12px;
    line-height: 17px;
    color: var(--text-white);
  }

  /* Back */
  .sky-photo {
    position: absolute;
    inset: 0;
    background:
      radial-gradient(ellipse 180px 40px at 20% 96%, rgba(255,255,255,0.75), transparent 70%),
      linear-gradient(180deg, var(--sky-deep) 0%, var(--sky-mid) 55%, var(--sky-light) 100%);
  }
  .airplane-photo {
    position: absolute;
    left: 60px;
    top: 70px;
    width: 380px;
    height: 90px;
    border-radius: 45px;
    transform: rotate(-14deg);
    background: linear-gradient(180deg, var(--plane-white) 0%, var(--plane-grey) 100%);
    opacity: 0.9;
  }
  .web-mark {
    position: absolute;
    right: 28px;
    bottom: 40px;
    display: flex;
    flex-direction: column;
    align-items: flex-end;
  }
  .web-mark-dot {
    width: 22px;
    height: 22px;
    border-radius: 50%;
    background: var(--logo-navy);
    margin: 0 120px 8px 0;
  }
  .web-mark-rule {
    width: 300px;
    height: 1px;
    background: var(--logo-navy);
    margin-bottom: 8px;
  }
  .web-address {
    font-family: "Cinzel", serif;
    font-weight: 600;
    font-size: 19px;
    letter-spacing: 4px;
    color: var(--logo-navy);
  }
</style>
</head>
<body>

  <section class="card card-front">
    <div class="brand">
      <span class="brand-dot" aria-hidden="true"></span>
      <span class="brand-name">MK TALLOW INSURANCE</span>
    </div>
    <div class="divider-main"></div>

    <div class="person">
      <div class="person-name">DANA WHITFIELD</div>
      <div class="person-title">Principal Agent</div>
      <div class="divider-person"></div>
      <ul class="contact-list">
        <li>
          <svg viewBox="0 0 12 12" aria-hidden="true"><path d="M2.5 1l2 2.2-1 1.3a6 6 0 0 0 4 4l1.3-1 2.2 2-1.2 1.5C5 11 1 7 1 2.2z" fill="#e0104f"/></svg>
          555-210-4187
        </li>
        <li>
          <svg viewBox="0 0 12 12" aria-hidden="true"><rect x="1" y="1" width="10" height="10" fill="none" stroke="#f2f2f2" stroke-width="1.4"/></svg>
          555 318 2260
        </li>
        <li>
          <svg viewBox="0 0 12 12" aria-hidden="true"><rect x="0.5" y="2" width="11" height="8" fill="#e0104f"/><path d="M0.5 2l5.5 4.5L11.5 2" fill="none" stroke="#151516" stroke-width="1"/></svg>
          dana@mktins.com
        </li>
      </ul>
    </div>

    <address class="address">
      48 Linden Parkway<br>
      Alder, Texas 70412<br>
      www.mktins.com
    </address>
  </section>

  <section class="card card-back">
    <div class="sky-photo" role="img" aria-label="Photograph of a bright blue sky with soft white clouds"></div>
    <div class="airplane-photo" role="img" aria-label="Photograph of a white airplane climbing to the upper right"></div>
    <div class="web-mark">
      <span class="web-mark-dot" aria-hidden="true"></span>
      <div class="web-mark-rule"></div>
      <div class="web-address">WWW.MKTINS.COM</div>
    </div>
  </section>

</body>
</html>
```